Organic CBD topicals needs product labels for body butters, roll on oils and massage oil candles

We are looking for product labels that fit our growing brand, We are yogi's making organic CBD infused topicals that help people with pain relief and healing through plant based creams and oils, naturally, without side effects. We have body butter balms that come in 2oz tins, we have massage oil candles in 6oz, mandala design tins with a lid, we have infused essential oils in frosted glass bottles with healing gemstone roller balls, we also make lip balms in both 1/2 oz tins and lip balm sticks, as well as a 2oz twist up body butter balm. I would like the labels to have a yogi/chakra feel to them. The body butter balms come in different strengths, so it would be great if the strongest 600mg start at the base chakra, using the chakre color scale and go up from there. 300mg, 150mg then pure CBD, then up the chakra scale for the other products, 1:1, 3:1 and 30:1 for the roll on essential oils and massage oil candles.

You can see our products here: www.lunavalebotanics.org

Kivo Body Butter Balm label 2 1/2" round.
Matching 2" label for the bottom of the tin with ingredients & instructions.
Massage Oil Candle label 1 1/2 round
Bottom of Candle label 2" round for ingredients & instructions
Spiraled Kivo Body Butter Label 4 1'2 wide x 2 1/2 tall Square
Twist up lip balm label can be 2 1/4 w x 1 1/2 tall
Lip Balm tin label 1" round

Target Market(s)

Everyone that has pain, injuries, headaches, skin conditions, etc... and wants to deal with them naturally, without big pharma and their terrible medicines that come with killer side effects.

Font styles to use
Serif
Sans Serif

Requirements
Must have
• A yogi look and feel, chakra colors, symbols and our logo featured prominently
Should not have
• a corporate look or feel

```html
<!DOCTYPE html>
<html lang="en">
<head>
<meta charset="utf-8">
<title>Kivo Organic Body Butter Salve – Label</title>
<link rel="stylesheet" href="https://fonts.googleapis.com/css2?family=Cinzel:wght@400;500&family=Lato:wght@300;400&display=swap">
<style>
  :root {
    --bg-center: #f5f5f5;
    --bg-edge: #a9a9a9;
    --olive: #a49d40;
    --mandala-purple: #a584c2;
    --mandala-orange: #c85a2c;
    --mandala-teal: #7ea8b3;
    --label-white: #ffffff;
    --brand-brown: #6e2012;
    --text-grey: #555555;
  }
  html, body {
    margin: 0;
    padding: 0;
    width: 1200px;
    height: 900px;
    overflow: hidden;
  }
  body {
    background: radial-gradient(ellipse at 40% 40%, var(--bg-center) 0%, #dcdcdc 45%, var(--bg-edge) 100%);
  }
  .label-canvas {
    display: block;
    width: 1200px;
    height: 900px;
  }
  .brand-name {
    font-family: "Cinzel", serif;
    font-weight: 500;
    font-size: 25px;
    fill: var(--brand-brown);
  }
  .brand-sub {
    font-family: "Cinzel", serif;
    font-weight: 500;
    font-size: 9px;
    letter-spacing: 1.5px;
    fill: var(--brand-brown);
  }
  .product-name {
    font-family: "Cinzel", serif;
    font-weight: 400;
    font-size: 33px;
    fill: var(--text-grey);
  }
  .product-type {
    font-family: "Lato", sans-serif;
    font-weight: 300;
    font-size: 19px;
    letter-spacing: 5.5px;
    fill: var(--text-grey);
  }
  .product-form {
    font-family: "Cinzel", serif;
    font-weight: 500;
    font-size: 31px;
    letter-spacing: 1px;
    fill: var(--brand-brown);
  }
  .product-strength {
    font-family: "Lato", sans-serif;
    font-weight: 300;
    font-size: 19px;
    fill: var(--text-grey);
  }
</style>
</head>
<body>
<svg class="label-canvas" viewBox="0 0 1200 900" xmlns="http://www.w3.org/2000/svg">
  <defs>
    <radialGradient id="chakraRing" gradientUnits="userSpaceOnUse" cx="614" cy="421" r="177">
      <stop offset="0.80" stop-color="#7ea8b3"/>
      <stop offset="0.86" stop-color="#c85a2c"/>
      <stop offset="0.92" stop-color="#b77aa6"/>
      <stop offset="1" stop-color="#a584c2"/>
    </radialGradient>
  </defs>

  <g class="label">
    <circle class="label-rim" cx="614" cy="421" r="206" fill="var(--olive)"/>
    <circle class="label-stitch" cx="614" cy="421" r="189" fill="none" stroke="var(--label-white)" stroke-width="3" stroke-dasharray="12 7"/>
    <circle class="label-spacer" cx="614" cy="421" r="181" fill="var(--label-white)"/>
    <circle class="mandala-band" cx="614" cy="421" r="177" fill="url(#chakraRing)" role="img" aria-label="Mandala ring pattern in purple, orange and teal chakra colours"/>
    <circle class="label-centre" cx="614" cy="421" r="143" fill="var(--label-white)" stroke="var(--olive)" stroke-width="3"/>

    <circle class="brand-seal" cx="612" cy="331" r="26" fill="var(--brand-brown)" opacity="0.85"/>
    <text class="brand-name" x="611" y="397" text-anchor="middle">LUNAVALE</text>
    <text class="brand-sub" x="612" y="410" text-anchor="middle">BOTANICS</text>

    <text class="product-name" x="606" y="445" text-anchor="middle">Kivo Organic</text>
    <text class="product-type" x="616" y="473" text-anchor="middle">BODY BUTTER</text>
    <text class="product-form" x="612" y="510" text-anchor="middle">SALVE</text>
    <text class="product-strength" x="612" y="535" text-anchor="middle">600mg</text>
  </g>
</svg>
</body>
</html>
```